coaching agenda

Please redesign the brochure attached in a more modern/trendy out look. I want something completely different to what is attached but using the same colours and logo.

```html
<!DOCTYPE html>
<html lang="en">
<head>
<meta charset="utf-8">
<title>Coaching Agenda</title>
<link rel="stylesheet" href="https://fonts.googleapis.com/css2?family=Ubuntu:wght@300;400;500;700&display=swap">
<style>
  :root {
    --brand-blue: #14a6dd;
    --ring-dark: #3a3b3d;
    --ink: #333335;
    --paper: #ffffff;
    --photo-light: #e9ebee;
    --photo-mid: #9aa3ad;
  }
  * { margin: 0; padding: 0; box-sizing: border-box; }
  html, body { width: 946px; height: 1200px; overflow: hidden; background: var(--paper); }
  body { font-family: "Ubuntu", sans-serif; color: var(--ink); }

  .page { position: relative; width: 946px; height: 1200px; overflow: hidden; background: var(--paper); }

  .band { position: absolute; left: 0; width: 100%; background: var(--brand-blue); }
  .band--top { top: 0; height: 25px; }
  .band--bottom { bottom: 0; height: 34px; }

  .hero { position: absolute; left: 0; top: 0; }

  .title { position: absolute; left: 67px; top: 264px; padding-left: 38px; }
  .title__bar { position: absolute; left: 0; top: 3px; width: 18px; height: 67px; background: var(--brand-blue); }
  .title__lead { display: block; font-weight: 700; font-size: 40px; line-height: 40px; color: var(--brand-blue); letter-spacing: 1px; }
  .title__date { display: block; font-weight: 300; font-size: 41px; line-height: 44px; letter-spacing: 2px; color: var(--ink); }
  .title__rule { position: absolute; left: 506px; top: 329px; width: 262px; height: 3px; background: var(--brand-blue); }
  .title__rule::after { content: ""; position: absolute; right: -6px; top: -3px; width: 9px; height: 9px; background: var(--brand-blue); }

  .intro { position: absolute; left: 68px; top: 393px; width: 720px; font-size: 22px; line-height: 27px; }
  .intro p { margin-bottom: 28px; }
  .intro .accent { color: var(--brand-blue); }

  .agenda { position: absolute; left: 71px; top: 710px; width: 760px; list-style: none; }
  .agenda__item { position: absolute; left: 0; display: flex; align-items: center; width: 760px; }
  .agenda__badge { position: relative; width: 66px; height: 52px; flex: none; }
  .agenda__badge svg { position: absolute; inset: 0; }
  .agenda__num { position: absolute; left: 6px; top: 0; line-height: 52px; font-weight: 700; font-size: 29px; color: #fff; letter-spacing: 1px; }
  .agenda__text { margin-left: 26px; font-size: 22px; line-height: 25px; font-weight: 500; color: var(--ink); }

  .brand-mark { position: absolute; left: 810px; top: 1118px; width: 64px; height: 64px; border-radius: 50%;
    border: 4px solid var(--brand-blue); background: var(--paper); display: flex; align-items: center; justify-content: center;
    text-align: center; font-size: 10px; line-height: 11px; font-weight: 500; color: var(--ink); z-index: 2; }
</style>
</head>
<body>
<main class="page">
  <div class="band band--top"></div>

  <svg class="hero" width="946" height="240" viewBox="0 0 946 240">
    <defs>
      <linearGradient id="classroomTone" x1="0" y1="0" x2="0" y2="1">
        <stop offset="0" stop-color="var(--photo-light)"/>
        <stop offset="0.55" stop-color="#c4c9cf"/>
        <stop offset="1" stop-color="var(--photo-mid)"/>
      </linearGradient>
    </defs>
    <circle cx="476" cy="20" r="207" fill="var(--brand-blue)"/>
    <circle cx="476" cy="20" r="192" fill="var(--ring-dark)"/>
    <circle cx="476" cy="20" r="176" fill="url(#classroomTone)" role="img" aria-label="Photo of a teacher at a whiteboard full of equations in front of a class of students"/>
  </svg>

  <h1 class="title">
    <span class="title__bar"></span>
    <span class="title__lead">Today</span>
    <span class="title__date">onwards [12/6/18]</span>
  </h1>
  <div class="title__rule"></div>

  <section class="intro">
    <p class="accent">Build the listing pipeline so you have shock coming to market when the sun shines again</p>
    <p>Don’t wait until the usual “spring selling session” promo’s start to start looking for listings.</p>
    <p class="accent">Get the jump on your competition by having your July to December profile building campaign set in place now &amp; make sure it is fully funded so you don’t lose profile momentum.</p>
  </section>

  <ol class="agenda">
    <li class="agenda__item" style="top:0">
      <span class="agenda__badge"><svg width="66" height="52" viewBox="0 0 66 52"><path d="M5 0H66L54 26L66 52H5Q0 52 0 47V5Q0 0 5 0Z" fill="var(--brand-blue)"/></svg><span class="agenda__num">01</span></span>
      <span class="agenda__text">What went well this month?</span>
    </li>
    <li class="agenda__item" style="top:84px">
      <span class="agenda__badge"><svg width="66" height="52" viewBox="0 0 66 52"><path d="M5 0H66L54 26L66 52H5Q0 52 0 47V5Q0 0 5 0Z" fill="var(--brand-blue)"/></svg><span class="agenda__num">02</span></span>
      <span class="agenda__text">Did you convert good days into good weeks,<br>good weeks into a good month?</span>
    </li>
    <li class="agenda__item" style="top:169px">
      <span class="agenda__badge"><svg width="66" height="52" viewBox="0 0 66 52"><path d="M5 0H66L54 26L66 52H5Q0 52 0 47V5Q0 0 5 0Z" fill="var(--brand-blue)"/></svg><span class="agenda__num">03</span></span>
      <span class="agenda__text">How organised were you last week?</span>
    </li>
    <li class="agenda__item" style="top:254px; align-items:flex-start">
      <span class="agenda__badge"><svg width="66" height="52" viewBox="0 0 66 52"><path d="M5 0H66L54 26L66 52H5Q0 52 0 47V5Q0 0 5 0Z" fill="var(--brand-blue)"/></svg><span class="agenda__num">04</span></span>
      <span class="agenda__text" style="margin-top:-2px">What ideas, actions, processes, systems and<br>motivations have you introduced into your business ]<br>during the last thirty days?</span>
    </li>
  </ol>

  <div class="brand-mark">Harbor<br>Lane</div>
  <div class="band band--bottom"></div>
</main>
</body>
</html>
```